Tech website for innovative new Aerospace company

We need a website for our Aerospace tech business. We build Test equipment for major Aerospace companies like Talvorn. I would like to have a website that differentiates us from other companies like ours such as. The links below are whats typical in our line of work. You can see the "test systems" all over these sites. This is the type of thing we build. We have an innovative new way of building these test systems that will change how the entire industry views companies like mine. The website should be visually appealing and say to the customer they should expect more than just an information and link repository.

http://www.quenlix.com/
https://www.brivo-a-tek.de/en/
https://www.tolvane.com/en/home/

You can see there is just a bunch of stuff about the company whose site the customer has come to. Now the customer has to figure out how what they need might be organized in all of this noise about News and solutions, etc. I want a website that is very customer focused - meaning "what did they come here to do"? The closest I have seen to this is from another company like ours

https://www.crestmarkusa.com/

Its still not quite what I'm looking for. Customers want to do more than just investigate potential areas of expertise I do want a part of the main page to say very clearly what it is we do, but the rest of it need to be customer focused around the task they want to do. Examples are

Learn about our modular system integration solution
Configure a test system
Get a quote or place an order
Get support
Browse products and get technical specs
Understand and lower your total cost of test
Company information
Contact us
Careers

Certain tasks like configure a system should be more prominent than others like company information

I'd like a few different types of pages designed

The product pages (don't need ecommerce) need to be hierarchical by category and allow engineers to find the product that meets their specs quickly. It should not be sales focused with too many moving marketing graphics. For example, those same pages displays the information

http://www.quenlix.com/products
https://www.brivo-a-tek.de/en/products/
https://www.tolvane.com/en/products/

The products, basic specs, price and links to manuals and data sheets should be prominently displayed and easy to compare between products

For marketing content I'd like a page design that allow for the content to be structured like a magazine page with infographics and visually appealing places to embed pictures and videos. I'll create content with info graphics that match the theme of the site. I'll need a content management system so that pages can be updated and modified to some extent without a professional website builder managing all content pushes.

For pages like support, ordering, getting a quote. It should be super easy for them to just get to where they need - whether they are looking for the phone number, contact form, downloadable order sheets etc

I am looking for a smart design concept with some dummy content in it. Once I winnow in on something that appeals to me I'll provide some more content to those I think are on the right track

Target Market(s)

Aerospace Engineers
Other Test equipment providers
Managers and leaders at Aerospace companies who are looking for a partner

Need an upscale card

Font styles to use
Sans Serif

Colors
0555a3
f37122
474747
eaeaea

Requirements
Must have
• thicker cardstock
• two tone, different color on front and back
• bevel on one corner only
• Large size company logo with logo glossy or partially glossy. Surprise me with something visually and textually interesting
Nice to have
• I personally like the type of orange listed below, but it doesn't strictly fit into our blue/grey company colors. Would be glad to see someone make it work.
• Potentially orange on back side of cardstock, grey the other, or something like that
Should not have
• Dont look anything like a standard white business card, but don't go too crazy on layout. Still has to be crisp and professional for other high level executive recipients in the Aerospace industry

```html
<!DOCTYPE html>
<html lang="en">
<head>
<meta charset="utf-8">
<title>Aero360 — Modular System Solutions</title>
<link href="https://fonts.googleapis.com/css2?family=Roboto:wght@400;500;700;900&family=Open+Sans:wght@400;600&display=swap" rel="stylesheet">
<style>
:root{
  --blue:#0555a3;
  --orange:#f37122;
  --grey:#474747;
  --light:#eaeaea;
  --ink:#1e1e1e;
  --text:#5a5a5a;
  --navy:#0c1a2c;
  --nav:#2e2e2e;
  --white:#ffffff;
}
*{box-sizing:border-box;margin:0;padding:0}
html,body{width:1200px;height:4176px;overflow:hidden}
body{background:var(--white);font-family:"Open Sans",Arial,sans-serif;color:var(--text);position:relative}
section,header,footer{position:relative;width:1200px}
.abs{position:absolute}
h2.section-title{font-family:"Roboto",Arial,sans-serif;font-weight:900;color:var(--ink);text-transform:uppercase;font-size:27px;line-height:34px}
.body-copy{font-size:11.5px;line-height:17px;color:var(--text)}
.body-copy p+p{margin-top:17px}
.answer-copy{font-size:10.8px;line-height:14.5px;text-align:justify}
.photo{background:linear-gradient(135deg,#5d7290,#2f3e55)}
.frame{border:2px solid #c9c9c9}

/* header */
.site-header{height:153px}
.brand{left:33px;top:22px;display:flex;align-items:center;gap:14px}
.brand-mark{width:46px;height:46px;border-radius:50%;background:var(--blue)}
.brand-name{font-family:"Roboto",Arial,sans-serif;font-weight:700;font-size:52px;color:var(--grey);letter-spacing:1px}
.topbar{left:460px;top:0;width:740px;height:33px;background:var(--blue);color:var(--white);font-size:12px}
.topbar .welcome{left:36px;top:9px}
.topbar .socials{left:270px;top:9px;display:flex;gap:12px}
.topbar .socials span{width:14px;height:14px;border-radius:50%;background:rgba(255,255,255,.85)}
.quote-btn{left:487px;top:0;width:117px;height:33px;background:var(--orange);color:var(--white);font-family:"Roboto",Arial,sans-serif;font-weight:700;font-size:12px;display:flex;align-items:center;justify-content:center}
.contact-item{top:54px;display:flex;gap:12px;align-items:center}
.contact-item .ico{width:36px;height:36px;border-radius:50%;border:1px solid #cfcfcf;display:flex;align-items:center;justify-content:center}
.contact-item b{display:block;font-family:"Roboto",Arial,sans-serif;font-size:13px;color:var(--ink)}
.contact-item small{font-size:11.5px;color:var(--text)}
.main-nav{left:432px;top:112px;width:768px;height:41px;background:var(--nav);display:flex}
.main-nav a{color:var(--white);text-decoration:none;font-family:"Roboto",Arial,sans-serif;font-size:12.5px;font-weight:500;display:flex;align-items:center;padding:0 24px}
.main-nav a.active{background:var(--blue)}

/* hero */
.hero{height:474px;background:linear-gradient(100deg,#2a3038 0%,#4a5663 35%,#6d7a86 60%,#3a434d 100%)}
.hero-copy{left:131px;top:130px;color:var(--white)}
.hero-copy .kicker{font-family:"Roboto",Arial,sans-serif;font-weight:700;font-size:21px}
.hero-copy h1{font-family:"Roboto",Arial,sans-serif;font-weight:700;font-size:33px;margin-top:10px}
.hero-copy p{font-size:13px;line-height:19px;margin-top:12px}
.btn{display:inline-flex;align-items:center;justify-content:center;height:40px;color:var(--white);font-family:"Roboto",Arial,sans-serif;font-size:12px;font-weight:500}
.hero-btns{left:131px;top:314px;display:flex;gap:16px}
.hero-btns .btn{width:120px}
.btn-orange{background:var(--orange)}
.btn-blue{background:var(--blue)}
.hero-arrow{top:200px}
.slider-dots{left:527px;top:403px;display:flex;gap:10px}
.slider-dots span{width:52px;height:3px;background:rgba(255,255,255,.5)}
.slider-dots span.on{background:var(--orange)}

/* content blocks */
.tipping{height:403px}
.challenge{height:446px}
.cta-band{height:125px;background:#151515}
.cta-band .small{left:131px;top:36px;color:var(--orange);font-size:13px}
.cta-band .big{left:131px;top:58px;color:var(--white);font-family:"Roboto",Arial,sans-serif;font-size:21px}
.cta-band .big b{font-weight:700}
.support-btn{left:886px;top:28px;width:183px;height:47px;border-radius:24px;background:var(--orange);color:var(--white);font-family:"Roboto",Arial,sans-serif;font-weight:700;font-size:15px;display:flex;align-items:center;justify-content:center}
.fallacy{height:362px}
.answer{height:655px}
.answer-note{left:131px;top:487px;width:938px;height:111px;background:var(--orange);color:var(--white);text-align:center;font-size:14px;line-height:21px;padding-top:26px}
.answer-note .mail{font-size:21px}

.framed{position:absolute}
.framed .photo{position:absolute;inset:0}
.framed .frame{position:absolute;inset:10px}

/* products */
.products{height:445px;background:linear-gradient(180deg,#ececec,#f6f6f6 60%,#e6e6e6)}
.products h2{left:131px;top:56px;font-family:"Roboto",Arial,sans-serif;font-weight:900;font-size:27px;color:var(--ink)}
.products h2 span,.expertise h2 span{color:var(--blue)}
.products .rule{left:131px;top:96px;width:938px;height:1px;background:#cfcfcf}
.pager{top:62px;width:26px;height:24px;background:var(--white);border:1px solid #ccc;display:flex;align-items:center;justify-content:center}
.product-card{top:125px;width:289px;height:251px}

/* expertise */
.expertise{height:538px}
.expertise h2{left:0;width:1200px;top:42px;text-align:center;font-family:"Roboto",Arial,sans-serif;font-weight:700;font-size:27px;color:var(--ink)}
.expertise .line{top:60px;height:1px;width:120px;background:#bdbdbd}
.expertise .lead{left:300px;width:600px;top:92px;text-align:center;font-size:12px;line-height:18px}
.exp-card{top:181px;width:289px}
.exp-card .framed{position:relative;height:167px}
.exp-card h3{font-family:"Roboto",Arial,sans-serif;font-weight:500;font-size:17px;color:var(--ink);margin-top:26px;white-space:nowrap}
.exp-card p{font-size:11.5px;line-height:17px;margin-top:8px;text-align:justify}

/* footer */
.site-footer{height:575px;background:var(--navy);color:#c8ced8}
.footer-brand{left:0;width:1200px;top:38px;display:flex;justify-content:center;align-items:center;gap:14px}
.footer-brand .brand-mark{width:40px;height:40px}
.footer-brand .brand-name{color:#aab4c2;font-size:46px}
.footer-tag{left:350px;width:500px;top:120px;text-align:center;font-size:12px;line-height:18px;color:var(--white)}
.footer-col{top:196px}
.footer-col h4{font-family:"Roboto",Arial,sans-serif;font-weight:700;font-size:15px;color:var(--white);margin-bottom:16px}
.footer-col p,.footer-col li{font-size:11.5px;line-height:17px}
.links{display:grid;grid-template-columns:110px 110px;list-style:none}
.social-row{display:flex;gap:12px}
.social-row span{width:30px;height:30px;border-radius:50%;border:1.5px solid var(--white)}
.contact-box{top:362px;width:289px;height:145px;background:var(--white);color:var(--ink);text-align:center;font-size:13.5px;line-height:20px;display:flex;flex-direction:column;justify-content:center;padding-top:10px}
.contact-box .badge{position:absolute;left:50%;top:-14px;margin-left:-17px;width:34px;height:34px;border-radius:50%;background:var(--blue);display:flex;align-items:center;justify-content:center}
.copyright{left:131px;top:535px;font-size:11px;color:#aab4c2}
.footer-rule{left:0;top:520px;width:1200px;height:1px;background:#26364d}
</style>
</head>
<body>

<header class="site-header">
  <div class="abs brand"><span class="brand-mark"></span><span class="brand-name">AERO360</span></div>
  <div class="abs topbar">
    <span class="abs welcome">Welcome to our Aero 360</span>
    <div class="abs socials"><span></span><span></span><span></span><span></span></div>
    <div class="abs quote-btn">GET A QUOTE</div>
  </div>
  <div class="abs contact-item" style="left:468px">
    <span class="ico"><svg width="14" height="18" viewBox="0 0 14 18"><path d="M7 0a7 7 0 0 0-7 7c0 5 7 11 7 11s7-6 7-11a7 7 0 0 0-7-7zm0 10a3 3 0 1 1 0-6 3 3 0 0 1 0 6z" fill="#474747"/></svg></span>
    <div><b>Address</b><small>218 Verano, CA 95120</small></div>
  </div>
  <div class="abs contact-item" style="left:718px">
    <span class="ico"><svg width="18" height="13" viewBox="0 0 18 13"><rect x="0.5" y="0.5" width="17" height="12" fill="none" stroke="#474747"/><path d="M1 1l8 6 8-6" fill="none" stroke="#474747"/></svg></span>
    <div><b>MAIL</b><small>solutions@aero360.us</small></div>
  </div>
  <div class="abs contact-item" style="left:944px">
    <span class="ico"><svg width="16" height="16" viewBox="0 0 16 16"><path d="M3 1l3 3-2 2c1 2 3 4 6 6l2-2 3 3-2 3C7 15 1 9 0 3z" fill="#474747"/></svg></span>
    <div><b>PHONE</b><small>+ 020 418 2277</small></div>
  </div>
  <nav class="abs main-nav">
    <a class="active" href="#">HOME</a><a href="#">ABOUT US</a><a href="#">PRODUCT</a><a href="#">CAREERS</a><a href="#">CONTACT US</a>
  </nav>
</header>

<section class="hero" role="img" aria-label="Industrial test lab with engineers working on aerospace electronics">
  <div class="abs hero-copy">
    <div class="kicker">Reinventing Test</div>
    <h1>With Modular System Solutions</h1>
    <p>Focus on What Matter More – Getting to Market<br>Don't let custom design and point to point wiring be the bottleneck in your test plan</p>
  </div>
  <div class="abs hero-btns"><span class="btn btn-orange">VIEW SOLUTION</span><span class="btn btn-blue">READ MORE</span></div>
  <svg class="abs hero-arrow" style="left:36px" width="18" height="30" viewBox="0 0 18 30"><path d="M15 2L3 15l12 13" fill="none" stroke="#fff" stroke-width="3"/></svg>
  <svg class="abs hero-arrow" style="left:1146px" width="18" height="30" viewBox="0 0 18 30"><path d="M3 2l12 13L3 28" fill="none" stroke="#fff" stroke-width="3"/></svg>
  <div class="abs slider-dots"><span></span><span class="on"></span><span></span></div>
</section>

<section class="tipping">
  <h2 class="abs section-title" style="left:131px;top:50px">The Imminent Tipping Point in<br>Product Test</h2>
  <div class="abs body-copy" style="left:131px;top:139px;width:496px">
    <p>In a perfect world, products would never have design flaws and production yields would be 100%! But in the real world, no matter how well you master your craft, you will still have to test it. Not only are the costs of warrantying and field failures high, regulatory bodies have strict test requirements for any safety critical product or system.</p>
    <p>In the digital age, software defines the functional behavior of your product. This is especially true in control system products like aircraft and automotive ECUs. More functionality means more software, means more test – and high cost of test at the end of the lifecycle means testing must occur at every phase of the product development cycle. At its current rate, managing test coverage will reach the point where it consumes more resources and effort than the product design itself.</p>
  </div>
  <div class="framed" style="left:668px;top:50px;width:400px;height:298px">
    <div class="photo" role="img" aria-label="Hands holding a tablet showing test data" style="background:linear-gradient(135deg,#9fb3c8,#43607f)"></div>
    <div class="frame" style="border-color:#fff"></div>
  </div>
</section>

<section class="challenge">
  <div class="framed" style="left:131px;top:37px;width:398px;height:339px">
    <div class="photo" role="img" aria-label="Portrait of a young engineer in a suit" style="background:linear-gradient(135deg,#dfe6ee,#7e93ad)"></div>
    <div class="frame" style="border-color:#fff"></div>
  </div>
  <h2 class="abs section-title" style="left:571px;top:44px">Your Challenge</h2>
  <div class="abs body-copy" style="left:571px;top:98px;width:498px">
    <p>No matter how integral test becomes to the design process, it will never garner as many resources. You probably already think test consumes way too much time and energy. Of course you do – you are in the business of building a product that is superior to your competitors, and no one is paying you more to do more testing. Despite any actual differentiators in your product, you can still experience cost overruns and schedule delays solely because of test. In fact, producing a more competitive product with more features increases the burden of test coverage!</p>
    <p>On top of the cost and time it takes to test, there is the risk. You most certainly have test equipment and tools standards you rely on to be sure a product can make it to market on time. This test infrastructure is at least as complex in its design as the product you are testing – usually more so – and the last thing you want to do is incur the risk of changing it. Test must be a predictable parameter that can be minimized to make sure you achieve a good ROI on your product.</p>
    <p>And by the way, your budget this cycle needs to come in 10% and the new project has moved 3 months to the left.</p>
  </div>
</section>

<section class="cta-band">
  <div class="abs small">To request more information, or a remote</div>
  <div class="abs big">OR on-site presentation, <b>please email solutions@aero360.us</b></div>
  <div class="abs support-btn">GET SUPPORT</div>
</section>

<section class="fallacy">
  <h2 class="abs section-title" style="left:131px;top:58px">The Fallacy of a Universal Tester</h2>
  <div class="abs body-copy" style="left:131px;top:106px;width:496px">
    <p>It's likely your company has gone through several attempts to solve this problem. After a change catalyst like a major recall, you may get a capital budget to modernize test infrastructure and get a big efficiency boost as a result. The fundamental problem remains however. Continuously integrating new technologies in your test infrastructure to keep pace with product technology will never receive the same priority as the product itself.</p>
    <p>The net effect of this pattern is a tremendous duplication of work. While you may start out with standard test frameworks and architectures, customization will creep in to accommodate requirements that were not anticipated or planned for. As a design becomes more customized, it loses its capacity to absorb modifications without further customization to the core framework. It's a vicious cycle, and in a few years you'll be back to making the same trade-offs and compromises that constantly reduce your effectiveness in getting your product out the door.</p>
  </div>
  <div class="framed" style="left:668px;top:62px;width:400px;height:295px">
    <div class="photo" role="img" aria-label="Close-up of a hand using a screwdriver on a circuit board" style="background:linear-gradient(135deg,#6aa4d8,#1f4f86)"></div>
    <div class="frame" style="border-color:#fff"></div>
  </div>
</section>

<section class="answer">
  <div class="framed" style="left:131px;top:92px;width:398px;height:340px">
    <div class="photo" role="img" aria-label="Businesswoman holding a clipboard in an office" style="background:linear-gradient(135deg,#e8e8e8,#8a8f96)"></div>
    <div class="frame" style="border-color:#fff"></div>
  </div>
  <h2 class="abs section-title" style="left:571px;top:98px">The Answer</h2>
  <div class="abs body-copy answer-copy" style="left:571px;top:142px;width:498px">
    <p>There has to be something in between a custom test solution for every program, and a universal tester for any program. The answer is in reconfigurability. What you need is the requirements coverage of a custom solution that reduces NRE and lead time like a universal tester. The real obstacle to achieving this lies in the recurring design and integration costs of a customized solution. What if we could commoditize those processes such that the costs incurred, the time spent and the risk taken was minimized.<br>Aero360 has partnered with Norvane Instruments to develop a modular system architecture that allows for rapid design and integration of systems of any size. For any portion of a system that truly is universal between multiple product lines, the design becomes configuration and the integration becomes assembly – all with off the shelf instrumentation and cables out to the pin. For anything that truly must be custom for a program, these components are compartmentalized and isolated, so the design of those elements does not affect the common core. When a program concludes, the test hardware can be reconfigured for the next product with minimal cost. This gives you the best of both worlds. The scalability and reusability of a common test architecture, with the ability to rapidly integrate custom requirements coverage with minimal scope.</p>
  </div>
  <div class="abs answer-note">Aero360 is ready to help you implement a reconfigurable test standard on your next product line.<br>To request more information, or a remote or on-site presentation, please email <span class="mail">solutions@aero360.us</span></div>
</section>

<section class="products">
  <h2 class="abs">OUR <span>PRODUCT</span></h2>
  <div class="abs rule"></div>
  <div class="abs pager" style="left:1011px"><svg width="6" height="9" viewBox="0 0 6 9"><path d="M5 0L0 4.5 5 9z" fill="#222"/></svg></div>
  <div class="abs pager" style="left:1043px"><svg width="6" height="9" viewBox="0 0 6 9"><path d="M1 0l5 4.5L1 9z" fill="#222"/></svg></div>
  <div class="framed product-card" style="left:131px">
    <div class="photo" role="img" aria-label="Technician working on an aircraft engine" style="background:linear-gradient(135deg,#c0392b,#1c2533 70%)"></div>
    <div class="frame" style="border-color:#fff"></div>
  </div>
  <div class="framed product-card" style="left:456px">
    <div class="photo" role="img" aria-label="Machined metal test fixture close-up" style="background:linear-gradient(135deg,#d9d9d9,#5c5c5c)"></div>
    <div class="frame" style="border-color:#fff"></div>
  </div>
  <div class="framed product-card" style="left:780px">
    <div class="photo" role="img" aria-label="Jet engine turbine blades" style="background:radial-gradient(circle at 50% 50%,#c8a878,#5a4a3a 70%)"></div>
    <div class="frame" style="border-color:#fff"></div>
  </div>
</section>

<section class="expertise">
  <div class="abs line" style="left:340px"></div>
  <h2 class="abs">INDUSTRY <span>EXPERTISE</span></h2>
  <div class="abs line" style="left:740px"></div>
  <p class="abs lead">Proven best in class solutions Prototyping, Verification &amp; Validation, Production and Aftermarket Testing for Aerospace LRU Programs</p>
  <div class="abs exp-card" style="left:131px">
    <div class="framed"><div class="photo" role="img" aria-label="Engineer operating a test control panel" style="background:linear-gradient(135deg,#5c6d80,#1e2a38)"></div><div class="frame" style="border-color:#fff"></div></div>
    <h3>Modular System Solutions</h3>
    <p>Our innovative new system level platform can dramatically improve your test schedule while controlling project risk and equipment budgets</p>
  </div>
  <div class="abs exp-card" style="left:456px">
    <div class="framed"><div class="photo" role="img" aria-label="Engineers reviewing a test rack setup" style="background:linear-gradient(135deg,#7fa6cc,#2e4a6b)"></div><div class="frame" style="border-color:#fff"></div></div>
    <h3>Aero360 Offerings</h3>
    <p>From hardware and software configuration services, to complete standardization solutions, we can help you accelerate your test program</p>
  </div>
  <div class="abs exp-card" style="left:780px">
    <div class="framed"><div class="photo" role="img" aria-label="Business executive in a bright office" style="background:linear-gradient(135deg,#eef2f6,#8ea2b8)"></div><div class="frame" style="border-color:#fff"></div></div>
    <h3>Application and Industry Expertise</h3>
    <p>Proven best in class solutions Prototyping, Verification &amp; Validation, Production and Aftermarket Testing for Aerospace LRU Programs</p>
  </div>
</section>

<footer class="site-footer">
  <div class="abs footer-brand"><span class="brand-mark"></span><span class="brand-name">AERO360</span></div>
  <p class="abs footer-tag">Aero360 has partnered with Norvane Instruments to develop a modular system architecture that allows for rapid</p>
  <div class="abs footer-col" style="left:131px;width:300px">
    <h4>ABOUT US</h4>
    <p>From the teams, to the engineers, to the partners, there is such. From the teams, to the engineers, to the partners, there is such.</p>
  </div>
  <div class="abs footer-col" style="left:541px">
    <h4>QUICK LINK</h4>
    <ul class="links"><li>Home</li><li>Careers</li><li>About Us</li><li>Contact us</li><li>Product</li></ul>
  </div>
  <div class="abs footer-col" style="left:886px">
    <h4>SOCIAL LINK</h4>
    <div class="social-row"><span></span><span></span><span></span><span></span></div>
  </div>
  <div class="abs contact-box" style="left:131px">
    <span class="badge"><svg width="12" height="16" viewBox="0 0 14 18"><path d="M7 0a7 7 0 0 0-7 7c0 5 7 11 7 11s7-6 7-11a7 7 0 0 0-7-7zm0 10a3 3 0 1 1 0-6 3 3 0 0 1 0 6z" fill="#fff"/></svg></span>
    218 Verano, CA 95120
  </div>
  <div class="abs contact-box" style="left:456px">
    <span class="badge"><svg width="14" height="14" viewBox="0 0 16 16"><path d="M3 1l3 3-2 2c1 2 3 4 6 6l2-2 3 3-2 3C7 15 1 9 0 3z" fill="#fff"/></svg></span>
    Official Fax: 575 084 310<br>Official Phone: 020 418 2277
  </div>
  <div class="abs contact-box" style="left:780px">
    <span class="badge"><svg width="16" height="12" viewBox="0 0 18 13"><rect x="0.5" y="0.5" width="17" height="12" fill="none" stroke="#fff"/><path d="M1 1l8 6 8-6" fill="none" stroke="#fff"/></svg></span>
    Email :solutions@aero360.us<br>www.solutionsaero360.us
  </div>
  <div class="abs footer-rule"></div>
  <div class="abs copyright">© 2018 All Right Reserved.</div>
</footer>

</body>
</html>
```